依頼詳細
【サイトの最大の要望】
①未経験の20代の求職者の登録者を増やす。
(短大卒・新卒・第二新卒・インターンシップの大学生)
②特に東京23区のエリアの強化

【強み】
・人材教育型採用支援
・未経験でも取れる
・アカデミー(代表自体が話す)

【ターゲット】
10代~20代の経理未経験者
(どちらかというと女性)
経理未経験の短大卒・新卒・第二新卒・インターンシップの大学生

【デザインについて】
・デザインテイストは「 モダン/ナチュラル/優しい/シンプル/清潔な/少し重厚感/ちょっと派手」

【参考サイト】
https://mofam.jp/
https://www.joblinvo.com/
https://senokuruto.jp/

【サイトマップ】
下記URL内のサイトマップを参照ください。
https://3.filebako.example/0722-b83d1e9a04fc2b67d51a0e4c88f7d2b1

■TOPページにGメニューとは別にデザインの入り口を必須で設けて頂きたいコン

テンツは以下となります。
(それ以外のページに関してはワークポッカーにお任せします)

サイトURL
http://tenuvel.com/
ページ数
1ページ
希望イメージ
シンプル 複雑
単色 カラフル
暗い 明るい
日常 高級
遊び心 厳粛
未来的 伝統的
女性的 男性的
希望する色
緑系、黄・オレンジ系、グレー系、黄・オレンジ系/グレー系/緑系(さし色)/ピンクベージュ
納品ファイル
• イラストレーター形式 (.ai)
• フォトショップ形式 (.psd)
• PNG形式 (.png)
補足説明
【店舗へのご連絡はおやめください】
ワークポッケ規約にもありますが、店舗への通常業務に支障が出るため、
直接電話等のお問い合わせをお控え頂きますよう、ご協力願います。

【素材写真】
下記よりダウンロードしてご使用ください。

また、ピクセモのカンプ画像をご使用ください。
選定後に正規データをお渡し致します。
(画像はマンスリーパック内でお願い致します。)
ワイヤーフレームを添付しますので、
参照ください。
先程の追記では説明不足でしてので、
補足致します。

サイトマップが確定する前に作成したワイヤーフレームになります。
決定版サイトマップを基に作成頂ければと思います。

ワイヤーフレームを添付することでデザインが全て同じになってしまう事を
避けたかったので、このタイミングで添付致しました。

ワイヤーフレームはあくまで参考として認識頂ければと思います。

宜しくお願い致します。

デザインの構成や色合いがとても素敵で訴求したいターゲットにも合っていると思いました。

選定させて頂きました。

引き続き、宜しくお願い致します。

```html
<!DOCTYPE html>
<html lang="ja">
<head>
<meta charset="utf-8">
<title>はなみちラボ｜経理・総務専門の人材育成</title>
<link rel="stylesheet" href="https://fonts.googleapis.com/css2?family=Noto+Sans+JP:wght@300;400;500;700&display=swap">
<style>
:root{
  --ink:#3c3c3c;
  --ink-soft:#6a6a6a;
  --panel-dark:#5a5a5a;
  --panel-darker:#4a4a4a;
  --white:#ffffff;
  --mist:#ececec;
  --sand:#e9e4df;
  --line:#bdbdbd;
}
*{box-sizing:border-box;margin:0;padding:0}
html,body{width:1200px;height:2680px;overflow:hidden}
body{font-family:"Noto Sans JP",sans-serif;color:var(--ink);background:var(--white);position:relative}
a{color:inherit;text-decoration:none}
.photo{position:absolute;display:block}

/* header */
.site-header{position:absolute;top:0;left:0;width:1200px;height:100px;z-index:5}
.brand{position:absolute;left:0;top:0;width:380px;height:100px;background:var(--panel-dark);color:var(--white);padding:16px 22px}
.brand-tagline{font-size:11px;font-weight:300;letter-spacing:.02em;opacity:.9;white-space:nowrap}
.brand-name{font-size:30px;font-weight:500;letter-spacing:.08em;margin-top:8px;line-height:1.2}
.header-tel{position:absolute;right:24px;top:12px;height:40px;background:var(--panel-darker);color:var(--white);display:flex;align-items:center;gap:10px;padding:0 16px;font-size:26px;font-weight:500;letter-spacing:.04em}
.header-tel small{font-size:10px;font-weight:300;line-height:1.2}

/* hero */
.hero{position:absolute;top:0;left:0;width:1200px;height:800px}
.hero .photo{inset:0;background:linear-gradient(180deg,#e8ecef 0%,#d8dde0 35%,#b7bab4 60%,#9ea09a 80%,#c9cbc8 100%)}
.global-nav{position:absolute;right:40px;top:110px;width:240px;background:rgba(255,255,255,.88);padding:16px 18px 14px}
.global-nav li{list-style:none;font-size:12px;padding:6px 0;border-bottom:1px solid #ddd;color:var(--ink-soft);white-space:nowrap}
.global-nav li::before{content:"›";margin-right:8px}
.nav-cta{display:block;margin-top:12px;background:var(--panel-dark);color:var(--white);text-align:center;font-size:12px;padding:8px}

/* headline */
.headline{position:absolute;left:250px;top:200px;writing-mode:vertical-rl;font-size:84px;font-weight:300;letter-spacing:0;color:var(--white);line-height:1;z-index:3}

/* academy */
.academy{position:absolute;top:800px;left:0;width:1200px;height:780px;background:var(--mist)}
.academy .photo{left:480px;top:120px;width:280px;height:660px;background:linear-gradient(180deg,#ececec 0%,#dcdad6 40%,#b9b6b1 75%,#8c8c8c 100%)}
.academy-menu{position:absolute;left:800px;top:120px;width:360px}
.academy-label{font-size:14px;color:var(--ink-soft);letter-spacing:.1em;border-bottom:1px solid var(--line);padding-bottom:10px}
.academy-menu li{list-style:none;font-size:30px;font-weight:400;padding:14px 0;border-bottom:1px solid var(--line);display:flex;justify-content:space-between;align-items:center;white-space:nowrap}
.academy-menu li.sub{font-size:24px}
.academy-menu svg{width:16px;height:16px;flex:0 0 16px}

/* feeds */
.feeds{position:absolute;top:1580px;left:0;width:1200px;height:820px;background:var(--sand)}
.feeds .model{left:490px;top:60px;width:220px;height:760px;background:linear-gradient(180deg,#e4dfda 0%,#cfc7bf 35%,#3e4250 60%,#6d6a68 100%)}
.feed{position:absolute;top:40px}
.feed-jobs{left:40px;width:410px}
.feed-column{left:740px;width:420px}
.feed-head{text-align:center;margin-bottom:26px}
.feed-head p{font-size:16px;color:var(--ink-soft);letter-spacing:.1em}
.feed-head h2{font-size:34px;font-weight:400;letter-spacing:.12em;margin-top:4px;display:flex;align-items:center;gap:16px;justify-content:center;white-space:nowrap}
.feed-head h2::before,.feed-head h2::after{content:"";flex:1;height:1px;background:var(--ink-soft)}
.entry{display:flex;gap:16px;margin-bottom:36px}
.entry .thumb{position:relative;flex:0 0 160px;height:110px}
.entry-text{flex:1;min-width:0}
.entry-text h3{font-size:15px;font-weight:500;margin-bottom:6px}
.entry-text p{font-size:12px;line-height:1.6;color:var(--ink-soft)}
.feed-column .entry{margin-bottom:22px}
.feed-column .entry .thumb{flex:0 0 150px;height:104px}

/* footer */
.site-footer{position:absolute;top:2400px;left:0;width:1200px;height:280px;background:var(--white)}
.footer-cta{position:absolute;top:12px;height:80px;display:flex;align-items:center;justify-content:center;color:var(--white);font-size:28px;letter-spacing:.08em}
.cta-contact{left:40px;width:540px;background:var(--ink-soft)}
.cta-tel{left:720px;width:440px;background:var(--panel-darker);gap:12px;font-weight:500}
.cta-tel small{font-size:11px;font-weight:300;line-height:1.3}
.footer-links{position:absolute;top:120px;left:40px;width:1120px;display:grid;grid-template-columns:repeat(5,1fr);gap:10px 20px}
.footer-links li{list-style:none;font-size:12px;color:var(--ink-soft)}
.footer-links li::before{content:"・"}
.copyright{position:absolute;bottom:14px;width:100%;text-align:center;font-size:11px;color:#999}
</style>
</head>
<body>

<header class="site-header">
  <div class="brand">
    <p class="brand-tagline">経理・総務専門の人材育成で、未経験からの就職を応援</p>
    <p class="brand-name">はなみちラボ</p>
  </div>
  <div class="header-tel">
    <svg width="26" height="20" viewBox="0 0 26 20"><rect x="1" y="1" width="24" height="18" rx="2" fill="none" stroke="#fff" stroke-width="2"/><path d="M7 6h12M7 10h12M7 14h8" stroke="#fff" stroke-width="2"/></svg>
    0120-000-431
    <small>受付時間<br>平日 9:00〜18:00</small>
  </div>
</header>

<section class="hero">
  <div class="photo" role="img" aria-label="高台の手すりに寄りかかる若い女性と街並みの写真"></div>
  <nav class="global-nav">
    <ul>
      <li>はなみちラボについて</li>
      <li>ステップ紹介</li>
      <li>はなみちカレッジの特徴</li>
      <li>就職実績</li>
      <li>求人一覧</li>
      <li>よくある質問</li>
      <li>はなみちコラム</li>
      <li>企業の方へ</li>
    </ul>
    <a class="nav-cta" href="#">資料請求・お問合せ</a>
  </nav>
</section>

<h1 class="headline">経理未経験でも大丈夫だった。</h1>

<section class="academy">
  <div class="photo" role="img" aria-label="白いブラウスの女性が立つ写真"></div>
  <div class="academy-menu">
    <p class="academy-label">未経験者セミナー</p>
    <ul>
      <li>はなみちカレッジ<svg viewBox="0 0 16 16"><path d="M5 2l6 6-6 6" fill="none" stroke="#3c3c3c" stroke-width="2"/></svg></li>
      <li class="sub">はなみちカレッジの実態日<svg viewBox="0 0 16 16"><path d="M5 2l6 6-6 6" fill="none" stroke="#3c3c3c" stroke-width="2"/></svg></li>
      <li>卒業生の声<svg viewBox="0 0 16 16"><path d="M5 2l6 6-6 6" fill="none" stroke="#3c3c3c" stroke-width="2"/></svg></li>
      <li>資料請求はこちら<svg viewBox="0 0 16 16"><path d="M5 2l6 6-6 6" fill="none" stroke="#3c3c3c" stroke-width="2"/></svg></li>
    </ul>
  </div>
</section>

<section class="feeds">
  <div class="photo model" role="img" aria-label="紺のトップスの女性が立つ写真"></div>

  <div class="feed feed-jobs">
    <div class="feed-head"><p>経理・総務専門の</p><h2>新着求人情報</h2></div>
    <article class="entry">
      <div class="photo thumb" role="img" aria-label="明るいオフィスの写真" style="background:linear-gradient(135deg,#cfc6bb,#8d8a86)"></div>
      <div class="entry-text"><h3>都内の会社で経理スタッフ募集</h3><p>未経験歓迎。研修制度あり。月給と勤務地、働き方の詳細はこちらから確認できます。</p></div>
    </article>
    <article class="entry">
      <div class="photo thumb" role="img" aria-label="会議室の写真" style="background:linear-gradient(135deg,#d9d4cc,#9a958e)"></div>
      <div class="entry-text"><h3>総務アシスタント（23区内）</h3><p>第二新卒歓迎。残業少なめ。先輩社員のサポートで基礎から学べる職場です。</p></div>
    </article>
    <article class="entry">
      <div class="photo thumb" role="img" aria-label="オフィスフロアの写真" style="background:linear-gradient(135deg,#c9bfb3,#7e7a76)"></div>
      <div class="entry-text"><h3>経理事務・未経験スタート</h3><p>新卒・短大卒歓迎。資格取得支援あり。長く安心して働ける環境を整えています。</p></div>
    </article>
  </div>

  <div class="feed feed-column">
    <div class="feed-head"><p>経理・総務のことがよくわかる</p><h2>はなみちコラム</h2></div>
    <article class="entry">
      <div class="photo thumb" role="img" aria-label="ノートとペンの写真" style="background:linear-gradient(135deg,#f1e2dc,#d8b9ae)"></div>
      <div class="entry-text"><h3>経理の仕事とは？</h3><p>一日の流れと必要なスキルをやさしく解説します。</p></div>
    </article>
    <article class="entry">
      <div class="photo thumb" role="img" aria-label="デスクと文具の写真" style="background:linear-gradient(135deg,#eee6e0,#c9b6ab)"></div>
      <div class="entry-text"><h3>簿記は何級から？</h3><p>未経験者がまず目指したい資格をご紹介します。</p></div>
    </article>
    <article class="entry">
      <div class="photo thumb" role="img" aria-label="パソコン作業の写真" style="background:linear-gradient(135deg,#e8e2da,#b9ada3)"></div>
      <div class="entry-text"><h3>面接で聞かれること</h3><p>よくある質問と答え方のコツをまとめました。</p></div>
    </article>
    <article class="entry">
      <div class="photo thumb" role="img" aria-label="手帳とカップの写真" style="background:linear-gradient(135deg,#f0dcd6,#cfa99d)"></div>
      <div class="entry-text"><h3>総務の魅力とは</h3><p>会社を支える仕事のやりがいをお伝えします。</p></div>
    </article>
  </div>
</section>

<footer class="site-footer">
  <a class="footer-cta cta-contact" href="#">お問合せはこちら</a>
  <div class="footer-cta cta-tel">
    <svg width="30" height="22" viewBox="0 0 26 20"><rect x="1" y="1" width="24" height="18" rx="2" fill="none" stroke="#fff" stroke-width="2"/><path d="M7 6h12M7 10h12M7 14h8" stroke="#fff" stroke-width="2"/></svg>
    0120-000-431
    <small>受付時間<br>平日 9:00〜18:00</small>
  </div>
  <ul class="footer-links">
    <li>はなみちラボについて</li>
    <li>はなみちカレッジの特徴</li>
    <li>求人一覧</li>
    <li>よくある質問</li>
    <li>お問合せ</li>
    <li>ステップ紹介</li>
    <li>卒業生の声</li>
    <li>はなみちコラム</li>
    <li>企業の方へ</li>
    <li>プライバシーポリシー</li>
  </ul>
  <p class="copyright">Copyright © はなみちラボ All Rights Reserved.</p>
</footer>

</body>
</html>
```